New online business - used mobile phones - needs unique eye catching web design that sets it apart

The Handset Bazaar
We are a new business looking for a rapid response for our web site design. We don't want a normal website....... we need to be creative - most important PLEASE view the attached files uploaded 3 March to ensure you get us :)
.
The Handset Bazaar buys new and damaged mobile phones from the public. A simple process they complete to sell their mobile to us; we want our website to reflect this.
Our website needs to be modern, edgy and fun, not corporate and definitely not like any other mobile phone buying site in the world today!!
Our name was taken from a play on the share/stock market which we have tried to bring into the design ....... it hasn't worked with early designs submitted. Now taking a different approach. Refer to new attached files which should help you visualise our concept.

We like layout from Sketch Flock – rtlbenoviqs #7132809 design as this is very close to our layout vision.
The first page to tell the public what we do, how we do it, and then they click to accept the instant online quote. (page two they complete details about the mobiles model & condition they are selling, then page three complete their personal details).
Our background preference is dark, blackboard or dark with slight texture
a) We love white on black/dark background either typewriter font or look like hand drawn refer to attached files & heronandfig.com.au site to see. Would Label font work???

b) Where the light blue colour is on #7132809 this needs to be like chromavell colour classic green, fern green or bright green, not fluorescent lime green or an insipid green.

c) The banner says The Handset Bazaar is open........... for buying mobiles for cash $$$ (we need people to know we BUY used/damaged phones)

d) We love colour either solid colour or looks like it has been coloured in on our dark background. Open to white or pastel background versions refer to attached coffee file.
We like Chromavell Orange 021,Haute Red,Dazzling Blue, Cyan Blue, Beetroot Purple, Island Green.
e) How it works – underneath this title put Our deal …………. It’s easy as…………..quote, post, get paid!!!
Quote – first circle hand drawn icon showing mobile phone & $ sign. Underneath it says .....Obtain Quote for Model & Condition
Post – second circle hand drawn icon show parcel. Underneath it says Free Post
Paid – third circle hand drawn icon showing large $ sign. Underneath it says Payment in Two Days
Plans - is swapped for wording- Get Market Quote with a large button which says GO or CLICK HERE (they click on the button & it takes them to the next page)
f) FAQ
Allow for six FAQ’s we will forward correct content to you for final design layout.

g) About Us
Please allow about a paragraph of text here, we will forward correct content to you for final design layout.
h) Contact Us
At the bottom where normal website have ………. home, contact details, blog, etc, please only put Email us & Call us, then social media icons for QV, Work Nest and Chirpel

I) LOGO We don’t have one yet, just put The Handset Bazaar at the top & it needs to be large sized font ................we are new and we need to push our name
If you are not clear on our vision ..........please email me and I will reply very quickly.
Thank you for taking the time to read & understand & get us:)

Target Market(s)

20-45 years any body with a spare smart phone that is lying around and they can get cash for. Target market could be slightly older to 50 but focus of 20-40's

Industry/Entity Type

Business

Number of Pages Required

3 page

Font styles to use
Other font styles liked:
• handwritten font or typewriter font

Requirements
Must have
• Read only attached files dated 4 March, tech error with other files, being removed.
• 1 Layout design of Sketch Flock – rtlbenoviqs #7132809
• 2 Hand drawn icons - refer to files
• 3 White font needs to look like hand written refer to heronandfig.com.au or typewriter font - large size font
• 4 Main colours are Black or dark background, green with white text, preference is hand drawn font. The three circles for quote, post & pay with hand drawn icons can be any colour ...... Purple for quote, orange for post & green for paid
• 5 Big green button underneath 3 circles quote/post/pay - customers click on big button to get instant quote
Nice to have
• Coloured in hand drawings as per file
• Great Hand drawings coloured in
Should not have
• NO template designs so it look like you just put some text & a photo. Don't fill the page with mobile phones, one or two is ok, mobile phone pictures date so fast.
• Cartoons

```html
<!DOCTYPE html>
<html lang="en">
<head>
<meta charset="utf-8">
<title>The Handset Bazaar – Sell your mobile for cash</title>
<link rel="stylesheet" href="https://fonts.googleapis.com/css2?family=Comfortaa:wght@400;700&family=Gochi+Hand&family=Caveat:wght@500&display=swap">
<style>
  :root {
    --green: #14c08c;
    --green-dark: #0e8f68;
    --green-pale: #a9ecd7;
    --ink: #161616;
    --night: #1b1b1b;
    --slate: #2a2a2a;
    --slate-line: #3a3a3a;
    --white: #ffffff;
    --muted: #8c8c8c;
    --hand: "Gochi Hand", cursive;
    --script: "Caveat", cursive;
    --body: "Comfortaa", sans-serif;
  }
  * { box-sizing: border-box; margin: 0; padding: 0; }
  html, body { width: 1200px; height: 2229px; overflow: hidden; }
  body {
    position: relative;
    background: var(--night);
    color: var(--white);
    font-family: var(--body);
  }
  .band { position: absolute; left: 0; width: 1200px; }
  .textured {
    background:
      radial-gradient(ellipse at 30% 40%, rgba(255,255,255,0.035), transparent 60%),
      radial-gradient(ellipse at 80% 70%, rgba(255,255,255,0.025), transparent 55%),
      var(--ink);
  }
  .abs { position: absolute; }
  .center { left: 0; width: 1200px; text-align: center; }

  /* header */
  .site-header { top: 0; height: 140px; }
  .brand {
    position: absolute; top: 34px; left: 0; width: 1200px;
    display: flex; justify-content: center; align-items: center; gap: 18px;
  }
  .brand-mark { width: 40px; height: 40px; border: 4px solid var(--green); border-radius: 6px; }
  .brand-name { font-family: var(--hand); font-size: 52px; line-height: 1; color: var(--white); }

  /* hero */
  .hero { top: 140px; height: 402px; background: var(--slate); }
  .hero-kicker { top: 34px; font-family: var(--script); font-size: 40px; line-height: 1; color: var(--green); }
  .hero-title { top: 78px; font-family: var(--hand); font-size: 68px; line-height: 1; color: var(--white); }
  .hero-art {
    left: 270px; top: 195px; width: 695px; height: 207px;
    background: linear-gradient(180deg, #3a3a3a 0%, #2f4a40 60%, #1e6a50 100%);
    border-radius: 4px 4px 0 0;
  }

  /* deal strip */
  .deal { top: 542px; height: 168px; }
  .deal-title { top: 22px; font-family: var(--hand); font-size: 54px; line-height: 1.06; color: var(--green); }

  /* steps */
  .steps { top: 710px; height: 358px; background: var(--slate); }
  .step { top: 0; width: 260px; margin-left: -130px; text-align: center; }
  .step-num {
    width: 34px; height: 34px; margin: -17px auto 0; border-radius: 50%;
    background: var(--green); border: 3px solid var(--white);
    font-family: var(--body); font-weight: 700; font-size: 17px; line-height: 28px; color: var(--white);
  }
  .step-icon { display: block; margin: 20px auto 0; }
  .step-title { margin-top: 10px; font-family: var(--hand); font-size: 34px; line-height: 1.1; color: var(--green); letter-spacing: 2px; }
  .step-text { margin: 4px auto 0; width: 170px; font-size: 14px; line-height: 1.35; color: #c8c8c8; }
  .step-arrow { top: 92px; }
  .rule { left: 176px; top: 243px; width: 846px; height: 1px; background: var(--slate-line); }
  .cta-label { top: 300px; font-family: var(--hand); font-size: 32px; color: var(--white); display: flex; align-items: center; gap: 12px; }

  .go-badge { left: 516px; top: 953px; width: 145px; height: 180px; z-index: 3; }

  /* faq */
  .faq { top: 1068px; height: 478px; }
  .section-title { font-family: var(--body); font-size: 30px; color: var(--green); }
  .faq-title { top: 92px; }
  .faq-q {
    height: 44px; background: var(--green); color: var(--ink);
    font-family: var(--hand); font-size: 16px; line-height: 44px; text-align: center;
    white-space: nowrap; padding: 0 6px;
  }
  .faq-a { width: 268px; font-size: 12px; line-height: 1.5; color: var(--muted); text-align: center; }

  /* about */
  .about { top: 1546px; height: 266px; background: var(--slate); }
  .about-title { top: 30px; }
  .about-text { left: 186px; top: 78px; width: 832px; font-size: 12px; line-height: 1.6; color: var(--muted); text-align: center; }
  .read-more {
    left: 503px; top: 192px; width: 172px; height: 46px; background: var(--green);
    clip-path: polygon(0 0, 100% 8%, 96% 100%, 3% 92%);
    font-family: var(--hand); font-size: 18px; line-height: 46px; text-align: center; color: var(--ink);
  }

  /* contact */
  .contact { top: 1812px; height: 241px; background: var(--night); }
  .contact-line { display: flex; align-items: flex-start; gap: 14px; }
  .contact-label { font-family: var(--hand); font-size: 19px; line-height: 1.1; letter-spacing: 1px; color: var(--white); }
  .contact-value { font-size: 14px; color: var(--green); margin-top: 3px; }
  .contact-rule { left: 168px; top: 124px; width: 220px; height: 1px; background: var(--slate-line); }
  .follow-title { left: 830px; top: 96px; font-family: var(--hand); font-size: 19px; line-height: 1.1; letter-spacing: 1px; }
  .social { left: 830px; top: 132px; display: flex; gap: 22px; }
  .social-item { display: flex; align-items: center; gap: 6px; font-family: var(--body); font-size: 14px; font-weight: 700; color: var(--green); }
  .social-item i { width: 12px; height: 12px; border: 2px solid var(--green); }

  .contact-panel { left: 424px; top: 1817px; width: 353px; height: 301px; z-index: 3; }
  .panel-shape { position: absolute; inset: 0; }
  .panel-title { top: 34px; left: 0; width: 353px; text-align: center; font-size: 24px; font-weight: 700; color: var(--white); }
  .field {
    position: absolute; background: var(--green-pale); color: #4a6d62;
    font-size: 10px; padding: 9px 10px; letter-spacing: 0.5px;
  }
  .send {
    position: absolute; left: 120px; top: 219px; width: 108px; height: 32px; background: var(--green-dark);
    clip-path: polygon(0 0, 100% 6%, 97% 100%, 2% 94%);
    font-size: 11px; font-weight: 700; line-height: 32px; text-align: center; color: var(--white);
  }

  /* footer */
  .site-footer { top: 2053px; height: 176px; }
  .footer-brand { top: 62px; font-family: var(--hand); font-size: 44px; color: var(--white); }
  .copyright { top: 128px; font-family: var(--hand); font-size: 16px; color: var(--green); }
</style>
</head>
<body>

<header class="band site-header textured">
  <div class="brand">
    <span class="brand-mark"></span>
    <span class="brand-name">The Handset Bazaar</span>
  </div>
</header>

<section class="band hero">
  <p class="abs center hero-kicker">The Handset Bazaar is open</p>
  <h1 class="abs center hero-title">for buying mobiles for cash !</h1>
  <div class="abs hero-art" role="img" aria-label="Hand-drawn illustration of a fist clutching banknotes, surrounded by mobile phones and flying green dollar bills"></div>
</section>

<section class="band deal textured">
  <h2 class="abs center deal-title">Our Deal .... It's Easy As......<br>quote, Post, Get Paid!!!</h2>
</section>

<section class="band steps">
  <div class="abs step" style="left:279px">
    <div class="step-num">1</div>
    <svg class="step-icon" width="90" height="56" viewBox="0 0 90 56" aria-hidden="true">
      <rect x="4" y="14" width="18" height="28" rx="3" fill="none" stroke="#4a4a4a" stroke-width="2"/>
      <rect x="68" y="14" width="18" height="28" rx="3" fill="none" stroke="#4a4a4a" stroke-width="2"/>
      <rect x="32" y="4" width="26" height="46" rx="4" fill="none" stroke="#ffffff" stroke-width="2.5"/>
      <rect x="37" y="12" width="16" height="28" fill="#14c08c"/>
      <text x="45" y="32" text-anchor="middle" font-family="Comfortaa, sans-serif" font-size="15" font-weight="700" fill="#161616">$</text>
    </svg>
    <div class="step-title">QUOTE</div>
    <p class="step-text">obtain quote for model &amp; condition !</p>
  </div>
  <svg class="abs step-arrow" style="left:421px" width="20" height="26" viewBox="0 0 20 26" aria-hidden="true"><path d="M3 3 L15 13 L3 23" fill="none" stroke="#555" stroke-width="5"/></svg>

  <div class="abs step" style="left:589px">
    <div class="step-num">2</div>
    <svg class="step-icon" width="170" height="56" viewBox="0 0 170 56" aria-hidden="true">
      <rect x="4" y="14" width="40" height="28" fill="none" stroke="#4a4a4a" stroke-width="2"/>
      <path d="M4 14 L24 30 L44 14" fill="none" stroke="#4a4a4a" stroke-width="2"/>
      <rect x="126" y="14" width="40" height="28" fill="none" stroke="#4a4a4a" stroke-width="2"/>
      <path d="M126 14 L146 30 L166 14" fill="none" stroke="#4a4a4a" stroke-width="2"/>
      <rect x="55" y="6" width="60" height="44" fill="#14c08c" stroke="#ffffff" stroke-width="2.5"/>
      <path d="M55 6 L85 30 L115 6" fill="none" stroke="#ffffff" stroke-width="2.5"/>
      <path d="M78 42 q6 -8 14 -4" fill="none" stroke="#ffffff" stroke-width="2"/>
    </svg>
    <div class="step-title">POST</div>
    <p class="step-text">Free post !</p>
  </div>
  <svg class="abs step-arrow" style="left:733px" width="20" height="26" viewBox="0 0 20 26" aria-hidden="true"><path d="M3 3 L15 13 L3 23" fill="none" stroke="#555" stroke-width="5"/></svg>

  <div class="abs step" style="left:905px">
    <div class="step-num">3</div>
    <svg class="step-icon" width="90" height="56" viewBox="0 0 90 56" aria-hidden="true">
      <text x="20" y="38" text-anchor="middle" font-family="Comfortaa, sans-serif" font-size="26" font-weight="700" fill="#4a4a4a">$</text>
      <text x="70" y="38" text-anchor="middle" font-family="Comfortaa, sans-serif" font-size="26" font-weight="700" fill="#4a4a4a">$</text>
      <text x="45" y="46" text-anchor="middle" font-family="Comfortaa, sans-serif" font-size="50" font-weight="700" fill="#14c08c">$</text>
      <text x="30" y="16" text-anchor="middle" font-family="Comfortaa, sans-serif" font-size="14" font-weight="700" fill="#ffffff">$</text>
    </svg>
    <div class="step-title">PAID</div>
    <p class="step-text">Payment into your bank account within two days !</p>
  </div>

  <div class="abs rule"></div>

  <div class="abs cta-label" style="left:210px">
    <span>Get Market Quote</span>
    <svg width="28" height="18" viewBox="0 0 28 18" aria-hidden="true"><path d="M2 9 L24 9 M16 2 L24 9 L16 16" fill="none" stroke="#14c08c" stroke-width="2.5"/></svg>
  </div>
  <div class="abs cta-label" style="left:730px">
    <svg width="28" height="18" viewBox="0 0 28 18" aria-hidden="true"><path d="M26 9 L4 9 M12 2 L4 9 L12 16" fill="none" stroke="#14c08c" stroke-width="2.5"/></svg>
    <span>Special Offers</span>
  </div>
</section>

<svg class="abs go-badge" viewBox="0 0 145 180" aria-label="Go to market quote">
  <polygon points="0,0 145,0 145,142 72.5,180 0,142" fill="#14c08c"/>
  <circle cx="72.5" cy="86" r="40" fill="none" stroke="#0d5a43" stroke-width="6"/>
  <path d="M72.5 34 V52 M72.5 120 V138 M20 86 H38 M107 86 H125" stroke="#0d5a43" stroke-width="6"/>
  <text x="72.5" y="95" text-anchor="middle" font-family="Comfortaa, sans-serif" font-size="24" font-weight="700" fill="#ffffff">GO</text>
</svg>

<section class="band faq textured">
  <h2 class="abs center section-title faq-title">FAQ !</h2>

  <div class="abs faq-q" style="left:173px; top:142px; width:265px">Q : How the handset bazaar works ?</div>
  <div class="abs faq-q" style="left:461px; top:142px; width:262px">Q : How the handset bazaar works ?</div>
  <div class="abs faq-q" style="left:745px; top:142px; width:268px">Q : How the handset bazaar works ?</div>
  <p class="abs faq-a" style="left:172px; top:202px">Get a quote for your model and condition, post it to us for free and we pay into your bank in two days.</p>
  <p class="abs faq-a" style="left:458px; top:202px">Get a quote for your model and condition, post it to us for free and we pay into your bank in two days.</p>
  <p class="abs faq-a" style="left:745px; top:202px">Get a quote for your model and condition, post it to us for free and we pay into your bank in two days.</p>

  <div class="abs faq-q" style="left:178px; top:316px; width:265px">Q : How the handset bazaar works ?</div>
  <div class="abs faq-q" style="left:466px; top:316px; width:265px">Q : How the handset bazaar works ?</div>
  <div class="abs faq-q" style="left:750px; top:316px; width:267px">Q : How the handset bazaar works ?</div>
  <p class="abs faq-a" style="left:176px; top:374px">Get a quote for your model and condition, post it to us for free and we pay into your bank in two days.</p>
  <p class="abs faq-a" style="left:464px; top:374px">Get a quote for your model and condition, post it to us for free and we pay into your bank in two days.</p>
  <p class="abs faq-a" style="left:750px; top:374px">Get a quote for your model and condition, post it to us for free and we pay into your bank in two days.</p>
</section>

<section class="band about">
  <h2 class="abs center section-title about-title">ABOUT US !</h2>
  <p class="abs about-text">The Handset Bazaar is a new kind of market for used phones. We buy new, old and damaged mobiles from the public and pay cash fast. There are no shops to visit and no forms to post. Tell us the model and the condition, accept our quote, then send the phone with our free postage pack. Once it arrives we check it against your description and pay the full amount into your bank account within two days. Spare phones lying in drawers lose value every month, so turn yours into cash today with a deal that is easy as quote, post, get paid.</p>
  <div class="abs read-more">Read More</div>
</section>

<section class="band contact">
  <div class="abs contact-line" style="left:168px; top:64px">
    <svg width="26" height="20" viewBox="0 0 26 20" aria-hidden="true"><rect x="1.5" y="1.5" width="23" height="17" fill="none" stroke="#14c08c" stroke-width="2"/><path d="M1.5 1.5 L13 11 L24.5 1.5" fill="none" stroke="#14c08c" stroke-width="2"/></svg>
    <div>
      <div class="contact-label">SEND US MAIL !</div>
      <div class="contact-value">hello@handsetbazaar.net</div>
    </div>
  </div>
  <div class="abs contact-rule"></div>
  <div class="abs contact-line" style="left:172px; top:140px">
    <svg width="20" height="32" viewBox="0 0 20 32" aria-hidden="true"><rect x="1.5" y="1.5" width="17" height="29" rx="3" fill="none" stroke="#14c08c" stroke-width="2"/><rect x="5" y="6" width="10" height="16" fill="none" stroke="#14c08c" stroke-width="1.5"/><circle cx="10" cy="26" r="1.6" fill="#14c08c"/></svg>
    <div>
      <div class="contact-label">CALL US NOW</div>
      <div class="contact-value">0800-246-8135</div>
    </div>
  </div>

  <div class="abs follow-title">FOLLOW US !</div>
  <div class="abs social">
    <span class="social-item"><i></i>Work Nest</span>
    <span class="social-item"><i></i>Chirpel</span>
    <span class="social-item"><i></i>QV</span>
  </div>
</section>

<div class="abs contact-panel">
  <svg class="panel-shape" viewBox="0 0 353 301" aria-hidden="true"><polygon points="0,0 353,0 353,240 176.5,301 0,240" fill="#14c08c"/></svg>
  <h2 class="abs panel-title">CONTACT US NOW</h2>
  <div class="field" style="left:24px; top:86px; width:148px; height:31px">NAME</div>
  <div class="field" style="left:178px; top:86px; width:150px; height:31px">EMAIL</div>
  <div class="field" style="left:24px; top:125px; width:304px; height:70px">MESSAGE</div>
  <div class="send">SEND</div>
</div>

<footer class="band site-footer textured">
  <div class="abs center footer-brand">The Handset Bazaar</div>
  <p class="abs center copyright">Copyrights © 2015, The Handset Bazaar. All Rights Reserved !</p>
</footer>

</body>
</html>
```